Re-style home page - eye-catching and unique design for social commerce website

We need a new concept design for TrindaMo's home page.
We don't want to make huge changes but creating a more professional and eye-catching style.

We need to look very serious like a professional services company and in the same time to look like a social network for e-commerce.

Our logo is very captive and you can use to creating something of harmonious.

This is a re-style and I'm excepted to see unique and fresh design like Clovaret.

Target Market(s)

e-commerce and social

Industry/Entity Type

Social

Number of Pages Required

1 page

Font styles to use
Serif
Sans Serif

Requirements
Must have
• An eye-catching result.
• Search bar with logo and Login How it works and business
• The slogan with login and signup.
• Footer links.
Nice to have
• I would like to open the home page and see only two clear ways:
• -Consumer
• --Search
• --The slogan
• --Login and Signup
• --How it works
• -Business
• --Go to Business area
• Background: City, Shopping.
Should not have
• Scrollbar style!

```html
<!DOCTYPE html>
<html lang="en">
<head>
<meta charset="utf-8">
<title>TrindaMo – Home</title>
<link href="https://fonts.googleapis.com/css2?family=Open+Sans:wght@400;600;700&family=PT+Sans:wght@400;700&display=swap" rel="stylesheet">
<style>
:root{
  --navy:#27235c;
  --white:#ffffff;
  --page:#f3f3f3;
  --card-line:#e4e4e4;
  --meta:#6b6b6b;
  --heart:#f05a5a;
  --red-a:#f0524c;
  --red-b:#d9344a;
  --overlay:rgba(58,58,58,0.86);
  --btn-grey:#c9c9c9;
  --social:#2d4487;
  --field:#f1f1f1;
  --footer-text:#444444;
}
*{box-sizing:border-box;margin:0;padding:0}
html,body{width:1200px;height:850px;overflow:hidden}
body{position:relative;background:var(--page);font-family:"Open Sans",Arial,sans-serif}

.site-header{position:absolute;left:0;top:0;width:1200px;height:74px;background:var(--navy);z-index:3}
.brand{position:absolute;left:100px;top:16px;display:flex;align-items:center;gap:10px;color:var(--white);font:700 32px/40px "Open Sans",Arial,sans-serif;letter-spacing:-0.5px}
.brand-dot{width:14px;height:14px;border-radius:50%;background:var(--white)}
.search{position:absolute;left:316px;top:19px;width:470px;height:39px;background:var(--white);border-radius:4px}
.search-btn{position:absolute;right:4px;top:3px;width:102px;height:33px;border-radius:3px;background:linear-gradient(var(--red-a),var(--red-b));color:var(--white);font:700 14px/33px "Open Sans",Arial,sans-serif;text-align:center;letter-spacing:.5px}
.main-nav a{position:absolute;top:30px;color:var(--white);font:400 14px/18px Arial,sans-serif;text-decoration:none}

.feed{position:absolute;left:0;top:74px;width:1200px;height:718px;overflow:hidden}
.card{position:absolute;width:311px;background:var(--white);border:1px solid var(--card-line);padding:9px}
.card-media{height:198px}
.card-meta{position:relative;height:50px;padding-top:16px}
.card-title{width:160px;font:400 12px/16px "Open Sans",Arial,sans-serif;color:var(--meta);text-transform:uppercase}
.card-stats{position:absolute;left:160px;top:16px;display:flex;align-items:center;gap:6px;font:400 12px/16px "Open Sans",Arial,sans-serif;color:var(--meta)}
.card-stats .likes{color:var(--heart);margin-left:8px;display:flex;align-items:center;gap:4px}
.card-stats svg{display:block}

.auth{position:absolute;left:299px;top:157px;width:564px;height:545px;background:var(--overlay);border-radius:4px;z-index:2;text-align:center}
.auth-login{position:absolute;right:6px;top:6px;width:107px;height:35px;border-radius:4px;background:var(--btn-grey);font:700 13px/35px "Open Sans",Arial,sans-serif;color:#222;letter-spacing:.5px}
.auth-brand{position:absolute;left:0;top:70px;width:564px;display:flex;justify-content:center;align-items:center;gap:10px;color:var(--white);font:700 34px/44px "Open Sans",Arial,sans-serif}
.auth-brand .brand-dot{width:16px;height:16px}
.social-btn{position:absolute;left:148px;top:167px;width:284px;height:51px;border-radius:3px;background:var(--social);color:var(--white);font:400 21px/51px Arial,sans-serif}
.divider{position:absolute;left:58px;top:240px;width:438px;height:22px}
.divider::before,.divider::after{content:"";position:absolute;top:11px;width:200px;height:1px;background:rgba(255,255,255,.3)}
.divider::before{left:0}.divider::after{right:0}
.divider span{color:var(--white);font:700 20px/22px "PT Sans",Arial,sans-serif}
.slogan{position:absolute;left:0;top:278px;width:564px;color:var(--white);font:700 33px/44px "PT Sans",Arial,sans-serif;letter-spacing:-0.5px;text-shadow:0 1px 3px rgba(0,0,0,.5)}
.field{position:absolute;left:130px;width:315px;height:40px;border-radius:3px;background:var(--field);border:1px solid #dcdcdc;text-align:left;padding-left:12px;font:700 14px/38px "PT Sans",Arial,sans-serif;color:#3a3a3a}
.signup{position:absolute;left:306px;top:472px;width:138px;height:39px;border-radius:3px;background:linear-gradient(var(--red-a),var(--red-b));color:var(--white);font:700 20px/39px "PT Sans",Arial,sans-serif}

.site-footer{position:absolute;left:0;top:792px;width:1200px;height:58px;background:var(--white);display:flex;justify-content:center;align-items:center;padding-right:18px;font:400 10px/12px Arial,sans-serif;color:var(--footer-text)}
.site-footer a{color:var(--footer-text);text-decoration:none}
.site-footer i{font-style:normal;margin:0 17px}
</style>
</head>
<body>

<header class="site-header">
  <div class="brand">TrindaMo <span class="brand-dot"></span></div>
  <div class="search"><div class="search-btn">SEARCH</div></div>
  <nav class="main-nav">
    <a href="#" style="left:834px">Login</a>
    <a href="#" style="left:912px">How it works</a>
    <a href="#" style="left:1034px">Business</a>
  </nav>
</header>

<main class="feed">
  <!-- row 1 -->
  <article class="card" style="left:-27px;top:2px">
    <div class="card-media" role="img" aria-label="Dreamcatcher with feathers in warm sunlight" style="background:linear-gradient(135deg,#f3ecd2,#d9c7a0 55%,#b79a6e)"></div>
    <div class="card-meta"><p class="card-title">Fullscreen post with info</p>
      <div class="card-stats"><svg width="12" height="8" viewBox="0 0 12 8"><path d="M0 4C2 0 10 0 12 4C10 8 2 8 0 4Z" fill="#6b6b6b"/><circle cx="6" cy="4" r="1.6" fill="#fff"/></svg>20924<span class="likes"><svg width="12" height="11" viewBox="0 0 12 11"><path d="M6 10L1 5C-1 2 2-1 6 2C10-1 13 2 11 5Z" fill="none" stroke="#f05a5a" stroke-width="1.2"/></svg>455</span></div></div>
  </article>
  <article class="card" style="left:306px;top:2px">
    <div class="card-media" role="img" aria-label="Man in a suit walking across a street" style="background:linear-gradient(160deg,#b7c3bd,#8e9b95 60%,#79847e)"></div>
    <div class="card-meta"><p class="card-title">Fullscreen without info</p>
      <div class="card-stats"><svg width="12" height="8" viewBox="0 0 12 8"><path d="M0 4C2 0 10 0 12 4C10 8 2 8 0 4Z" fill="#6b6b6b"/><circle cx="6" cy="4" r="1.6" fill="#fff"/></svg>22503<span class="likes"><svg width="12" height="11" viewBox="0 0 12 11"><path d="M6 10L1 5C-1 2 2-1 6 2C10-1 13 2 11 5Z" fill="none" stroke="#f05a5a" stroke-width="1.2"/></svg>519</span></div></div>
  </article>
  <article class="card" style="left:638px;top:2px">
    <div class="card-media" role="img" aria-label="Folded colourful fabric on a chair stand" style="background:linear-gradient(150deg,#e9b98c,#dfe6ec 40%,#cfd9e1)"></div>
    <div class="card-meta"><p class="card-title">Video post without info</p>
      <div class="card-stats"><svg width="12" height="8" viewBox="0 0 12 8"><path d="M0 4C2 0 10 0 12 4C10 8 2 8 0 4Z" fill="#6b6b6b"/><circle cx="6" cy="4" r="1.6" fill="#fff"/></svg>13183<span class="likes"><svg width="12" height="11" viewBox="0 0 12 11"><path d="M6 10L1 5C-1 2 2-1 6 2C10-1 13 2 11 5Z" fill="none" stroke="#f05a5a" stroke-width="1.2"/></svg>446</span></div></div>
  </article>
  <article class="card" style="left:971px;top:2px">
    <div class="card-media" role="img" aria-label="Fashion model posing in a paper ribbon dress" style="background:linear-gradient(135deg,#efe4d8,#c9a98c 60%,#8a6650)"></div>
    <div class="card-meta"><p class="card-title">Fullscreen ribbon post</p>
      <div class="card-stats"><svg width="12" height="8" viewBox="0 0 12 8"><path d="M0 4C2 0 10 0 12 4C10 8 2 8 0 4Z" fill="#6b6b6b"/><circle cx="6" cy="4" r="1.6" fill="#fff"/></svg>16398</div></div>
  </article>

  <!-- row 2 -->
  <article class="card" style="left:-27px;top:300px">
    <div class="card-media" role="img" aria-label="Sea waves breaking over dark rocks" style="background:linear-gradient(170deg,#36525e,#5b7a86 45%,#2b3a40)"></div>
    <div class="card-meta"><p class="card-title">Video post with info</p>
      <div class="card-stats"><svg width="12" height="8" viewBox="0 0 12 8"><path d="M0 4C2 0 10 0 12 4C10 8 2 8 0 4Z" fill="#6b6b6b"/><circle cx="6" cy="4" r="1.6" fill="#fff"/></svg>5858<span class="likes"><svg width="12" height="11" viewBox="0 0 12 11"><path d="M6 10L1 5C-1 2 2-1 6 2C10-1 13 2 11 5Z" fill="none" stroke="#f05a5a" stroke-width="1.2"/></svg>91</span></div></div>
  </article>
  <article class="card" style="left:306px;top:300px">
    <div class="card-media" role="img" aria-label="Dark moody portrait of a woman" style="background:linear-gradient(150deg,#4a4645,#2a2726 60%,#1c1a19)"></div>
    <div class="card-meta"><p class="card-title">Simple fullwidth image post</p>
      <div class="card-stats"><svg width="12" height="8" viewBox="0 0 12 8"><path d="M0 4C2 0 10 0 12 4C10 8 2 8 0 4Z" fill="#6b6b6b"/><circle cx="6" cy="4" r="1.6" fill="#fff"/></svg>13534<span class="likes"><svg width="12" height="11" viewBox="0 0 12 11"><path d="M6 10L1 5C-1 2 2-1 6 2C10-1 13 2 11 5Z" fill="none" stroke="#f05a5a" stroke-width="1.2"/></svg>124</span></div></div>
  </article>
  <article class="card" style="left:638px;top:300px">
    <div class="card-media" role="img" aria-label="Narrow old town street with colourful houses" style="background:linear-gradient(120deg,#a6765a,#c9b49a 45%,#8c4b3a)"></div>
    <div class="card-meta"><p class="card-title">Simple image post</p>
      <div class="card-stats"><svg width="12" height="8" viewBox="0 0 12 8"><path d="M0 4C2 0 10 0 12 4C10 8 2 8 0 4Z" fill="#6b6b6b"/><circle cx="6" cy="4" r="1.6" fill="#fff"/></svg>10144<span class="likes"><svg width="12" height="11" viewBox="0 0 12 11"><path d="M6 10L1 5C-1 2 2-1 6 2C10-1 13 2 11 5Z" fill="none" stroke="#f05a5a" stroke-width="1.2"/></svg>130</span></div></div>
  </article>
  <article class="card" style="left:971px;top:300px">
    <div class="card-media" role="img" aria-label="Woman with windswept platinum hair" style="background:linear-gradient(135deg,#dfe3e6,#c4ccd2 50%,#a7b0b5)"></div>
    <div class="card-meta"><p class="card-title">Simple post with sidebar</p>
      <div class="card-stats"><svg width="12" height="8" viewBox="0 0 12 8"><path d="M0 4C2 0 10 0 12 4C10 8 2 8 0 4Z" fill="#6b6b6b"/><circle cx="6" cy="4" r="1.6" fill="#fff"/></svg>547</div></div>
  </article>

  <!-- row 3 -->
  <article class="card" style="left:-27px;top:590px">
    <div class="card-media" role="img" aria-label="Portrait of a blonde woman in a coat" style="background:linear-gradient(160deg,#e6e1da,#b8a894 60%,#7d6d5c)"></div>
  </article>
  <article class="card" style="left:306px;top:590px">
    <div class="card-media" role="img" aria-label="Misty beach with a pier" style="background:linear-gradient(180deg,#d9c8c4,#b9a7a3 60%,#8f7e7a)"></div>
  </article>
  <article class="card" style="left:638px;top:590px">
    <div class="card-media" role="img" aria-label="City rooftops under a winter sky" style="background:linear-gradient(180deg,#c6d6e1,#7b93a6 60%,#4f6272)"></div>
  </article>
  <article class="card" style="left:971px;top:590px">
    <div class="card-media" role="img" aria-label="Two women in a sunlit ruined hall" style="background:linear-gradient(160deg,#d7dcc8,#6f7a5a 55%,#3c4632)"></div>
  </article>
</main>

<section class="auth">
  <div class="auth-login">LOGIN</div>
  <div class="auth-brand">TrindaMo <span class="brand-dot"></span></div>
  <div class="social-btn">Login with Linkora</div>
  <div class="divider"><span>or</span></div>
  <h1 class="slogan">Shop Directly from your profile</h1>
  <div class="field" style="top:344px">Username</div>
  <div class="field" style="top:407px">Password</div>
  <div class="signup">Sign Up</div>
</section>

<footer class="site-footer">
  <a href="#">ABOUT TRINDAMO</a><i>|</i>
  <a href="#">BLOG</a><i>|</i>
  <a href="#">BUSINESS</a><i>|</i>
  <a href="#">TERMS &amp; PRIVACY</a><i>|</i>
  <a href="#">HELP</a><i>|</i>
  <a href="#">POMELO APP</a><i>|</i>
  <a href="#">KESTREL APP</a>
</footer>

</body>
</html>
```